N.B: The designer that we will select his/her designs will earn an extra 320$!
We are looking for branding expert to create and develop a full branding image for our company.
We are a digital and social media agency based in Lebanon (Middle East) catering the Gulf area as Dubai, Saudi Arabia...
Our services are:
- Digital Strategy
- Community Management
- Social Content Creation
- Web and Mobile Development
- Online Media Planing and booking
In another word we are a full fledged digital agency whereby we provide 360 degrees digital experience.
We are aiming to cooperate with a branding design expert to provide us with out of the box and updated futuristic branding image.
The job will include design of :
- Logo (Kindle Bay Studio) "ME=Middle East" and it has indirect meaning "ME=My Self" but we want to focus on the "A" of the accelerate same as the "F" of Plazebook" & "T" of Chirrup and the "V" of Ivy.... especially that we are willing to change the "ME" when we open in Dubai by replacing the "Me" by UAE, KSA, Kuwait, Qatar, Paris... so in each country we will change it accordingly to the country of operation to be as (Kindle Paris Studio)
- Business cards
- Corporate Identity (letterhead, envelops...)
- Power Point Presentation
- Branded ads ( magazines, posters, online ads, watermarks...)
- New Slogan
- Pantone and fonts description
Our current slogan is "Beyond the pixel curtain"
We are looking for a strong branding identity at the same time simple, creative with digital colors which differentiate us from other digital agencies.
Target Market(s)
Middle East and Europe
Industry/Entity Type
Catering
Look and feel

```html
<!DOCTYPE html>
<html lang="en">
<head>
<meta charset="utf-8">
<title>Kindle Bay Studio — Business Card</title>
<link rel="stylesheet" href="https://fonts.googleapis.com/css2?family=Roboto+Condensed:wght@400;700&display=swap">
<style>
  :root {
    --brand-red: #d41c13;
    --ink: #111111;
    --label-ink: #1a1a1a;
    --card-white: #ffffff;
    --stage-light: #f4f4f4;
    --stage-dark: #c9c9c9;
    --back-light: #ffffff;
    --back-dark: #9a9a9a;
    --text-font: "Roboto Condensed", "Arial Narrow", sans-serif;
  }
  * { box-sizing: border-box; margin: 0; padding: 0; }
  html, body { width: 1200px; height: 861px; overflow: hidden; }
  body {
    position: relative;
    font-family: var(--text-font);
    background: radial-gradient(ellipse at 55% 55%, var(--stage-light) 0%, #e2e2e2 55%, var(--stage-dark) 100%);
    color: var(--ink);
  }
  .side-label {
    position: absolute;
    font-size: 22px;
    letter-spacing: 1.5px;
    color: var(--label-ink);
  }
  .side-label--front { left: 87px; top: 184px; }
  .side-label--back { left: 1024px; top: 639px; }

  .card {
    position: absolute;
    border-radius: 28px;
    overflow: hidden;
    text-align: center;
  }
  .card--back {
    left: 600px; top: 38px; width: 569px; height: 569px;
    background: radial-gradient(circle at 50% 48%, var(--back-light) 0%, #ececec 40%, var(--back-dark) 100%);
    box-shadow: 2px 4px 10px rgba(0,0,0,0.35);
  }
  .card--front {
    left: 64px; top: 225px; width: 578px; height: 578px;
    background: var(--card-white);
    box-shadow: 2px 4px 10px rgba(0,0,0,0.35);
  }

  .brand-square {
    position: absolute;
    background: var(--brand-red);
  }
  .card--front .brand-square { left: 244px; top: 45px; width: 87px; height: 87px; border-radius: 12px; }
  .card--back .brand-square { left: 193px; top: 95px; width: 180px; height: 180px; border-radius: 24px; }

  .brand-name {
    position: absolute;
    left: 0; right: 0;
    font-weight: 700;
    color: var(--ink);
    white-space: nowrap;
  }
  .card--front .brand-name { top: 142px; font-size: 30px; }
  .card--back .brand-name { top: 296px; font-size: 60px; line-height: 76px; }

  .slogan-bar {
    position: absolute;
    left: 85px; top: 412px; width: 416px; height: 29px;
    border-radius: 15px;
    background: var(--brand-red);
    font-size: 20px;
    line-height: 29px;
    color: var(--ink);
  }
  .website {
    position: absolute;
    left: 0; right: 0; top: 514px;
    font-size: 21px;
    color: var(--ink);
  }

  .contact {
    position: absolute;
    left: 0; right: 0; top: 293px;
    font-size: 22px;
    line-height: 26px;
  }
  .office-line {
    position: absolute;
    left: 0; right: 0; top: 474px;
    font-size: 19px;
  }
  .services-band {
    position: absolute;
    left: 0; right: 0; bottom: 0; height: 72px;
    background: var(--brand-red);
    color: var(--card-white);
    font-size: 18px;
    line-height: 23px;
    padding-top: 12px;
  }
  .services-band span { margin: 0 7px; }
</style>
</head>
<body>
  <div class="side-label side-label--front">FRONT SIDE</div>
  <div class="side-label side-label--back">BACK SIDE</div>

  <section class="card card--back">
    <div class="brand-square"></div>
    <div class="brand-name">Kindle Bay Studio</div>
    <div class="slogan-bar">Beyond the pixel curtain</div>
    <div class="website">WWW.KINDLEBAYSTUDIO.COM</div>
  </section>

  <section class="card card--front">
    <div class="brand-square"></div>
    <div class="brand-name">Kindle Bay Studio</div>
    <div class="contact">NAME<br>MOBILE PHONE</div>
    <div class="office-line">HEAD OFFICE ADDRESS, TELP AND FAX HERE</div>
    <div class="services-band">
      <div><span>Digital Strategy</span><span>Community Management</span><span>Social Content Creation</span></div>
      <div><span>Web and Mobile Development</span><span>Online Media Planing and booking</span></div>
    </div>
  </section>
</body>
</html>
```